I am in need of a Fact Sheet to distribute to clients about my new hotel opening in October 2012.

It can be single or double sided.

I can provide 4 existing photos of show rooms
and example of our hotel's story (we are not to keen on the "story presentation" as it currently exists)
I can provide Brand spec logos as well

Suggested Verbiage will be provided
Updates

I have uploaded examples of Fact Sheets from other properties; fyi I do not think that the examples are as detailed as they should be however, I do like the feel of the bold colors, etc.

I have also uploaded a few pictures of room that may be used at your discretion

I have uploaded Global Logo's (I have another project that is being worked to modify the logo with area indicator); I will forward any updated logos as soon as possible.

Please remember Bold and Upscale when designing.

I will extend the deadline

Reason: I just uploaded additional information; therefore I have extended the deadline in order to give more time.

Reason: I will not be available to make a decision until then, I decided to offer more time.

Reason: I just returned from vacation; begin reviewing entries today, 8/21

Use either the Crimson or Teal Color for background, border, etc, (your choice):

Crimsom

Pantone: 1935C

C: 1 / M: 100 / Y: 51/ K: 10

R: 195 / G: 0 / B: 69        

Pantone: 3272C
C: 99 / M: 0 / Y: 55 / K: 0
R: 0 / G: 165 / B: 153

 

FRONT OF PAGE:

Add under logo at top:

New Orleans Garden District

 

Add address to right of logo:

4817 Marlowe Terrace

New Orleans, LA  70130

504-718-2946

 
Verbiage for front of page:

Our Story.

The newest upscale property in the historic garden district!  Under the oak trees, along the Wexford Street Car line the hotel is just minutes from all business and leisure attractions for which New Orleans is famous.

 

Through our doors you will find a fusion of two worlds, the modern conveniences of new construction and the charm of historic New Orleans.  You will also find Corvel's Bar & Bistro featuring traditional New Orleans cuisine and cocktails.

 

Just steps from the hotel experience wonderful architecture and gardens into which are tucked famous New Orleans restaurants and lounges or simply stumble upon famous New Orleans landmarks.

 

 (USE the Fleur de Lis symbol for the bullets)

 

Hotel Features:

·          Complimentary Wireless Internet

·          Valet Parking

·          24 Hour Business Center

·          State of the Art Fitness Center

·          Spa-like bathrooms

·          Lunessa Bath Amenities

·          In-Room Safes

·          Corvel's Bar & Bistro featuring Breakfast, Dinner and Cocktails

·          Room Service

·          24 Hour Pantry with grab and go options

·          Pet Friendly

·          Valet and Guest Laundry Services

·          View of the Wexford Streetcar Line

 

Meeting Rooms:

·          Tressel Room - offers a variety of setups up to 80 guests

·          Hemberline Boardroom - spacious meeting room with conference seating up to twelve

                                **Catering services and menus available.

 

Utilize pictures from the murals provided

 

BACK OF PAGE

 

Local Attractions

·         Hollowmere Heritage Museum

·         Pellingham Institute-Zoo, Aquarium & Insectarium

·         Quillon Steamboat

·         Dorvik’s Casino

·         Brackwater Gallery of Fine Art

·         St. Ambrel Catherdal

·         Tullis Square

·         The Marqueta

·         Fernhollow Children’s Museum 

 

 

Must Do:

·         Ride the Wexford Avenue Streetcar

·         Shopping & Dining on Pennick Street

·         Eat beignets at Café Belvaro

·         Garden District Tour—by foot or horse drawn carriage

·         Visit Rory Calloways

·         Tour the Hollowmere Heritage Museum

·         Relax in Ashgrove Park

·         Ride the Quillon Steamboat

·         Visit St. Ambrel Cathedral

·         Cemetery Tour

 

Must See

·         Garden District

·         Pennick Street

·         French Quarter

·         Tamsin Street

·         Art Galleries on Harrow Street

·         Whitcombe Cemetery No. 1

·         Guthrie Street: best place to hear jazz

·         Dunmore Market

 

Don’t Forget

·         Beignet mix from Café Belvaro

·         Hurricane glass from Rory Calloways

·         Signed menus from our local chefs (Tobias Wrenfield, Calvin Morrow, Peter Hollis just to name a few)

·         Trinkets from the Dunmore Market

·         Pictures from a streetcar ride

·         Indulge in a Korvan Beer or Rootbeer

·         Try Granny Mabel’s Praline

·         Sample Louisiana Gumbo

 

Add to either front or back 
 

Hotel Contact Information.

Derek Manning, General Manager

Lydia Courten, Director of Sales

Karen Vosser, Area Sales Manager

 

GDS Codes  (regular bullets for below okay and smaller font)

·         Sabre AA 493217

·         Nimbra AM  MSY080

·         Worldspan TW 7861

·         Corsano  UA 89731

·         Veltrix  IN MSYIN

 

We are Here.

Include Map
Include address with phone number again

    4817 Marlowe Terrace
    New Orleans, LA  70130
    504-718-2946

Target Market(s)

Equal Men/Women; World Travelers looking for lodging that isn't a standard hotel; boutique hotel

Industry/Entity Type

Hotel

Requirements
Must have
• The Hotel Saffrine New Orleans Garden District is the premier upscale property located in New Orleans Garden District. Under the oak trees, along the Wexford Avenue Streetcar Line, the hotel is just minutes from all business and leisure attractions for which New Orleans is famous. Within the hotel enjoy a taste of New Orleans cocktails and cuisine in Corvel's Bar & Grill. Just steps from the hotel experience wonderful architecture and gardens into which are tucked famous New Orleans restaurants and lounges. The streetcar will take you everywhere you need to go from the French Quarter to One Talbrook Plaza to Marchetti University.

Must Do:
• Ride the Wexford Avenue Streetcar
• Shopping & Dining on Pennick Street
• Eat beignets at Café Belvaro
• Garden District Tour—by foot or horse drawn carriage
• Visit Rory Calloways
• Tour the Hollowmere Heritage Museum
• Relax in Ashgrove Park
• Ride the Quillon Steamboat
• Visit St. Ambrel Cathedral
• Cemetery Tour
• Tour the Art Galleries on Harrow Street

Must See
• Garden District
• Pennick Street
• French Quarter
• Tamsin Street
• Art Galleries on Harrow Street
• Brindle Street Streetcar Line
• Whitcombe Cemetery No. 1
• Café Belvaro
• Tullis Square
• Dunmore Market

Don’t Forget
• Beignet mix from Café Belvaro
• Hurricane glass from Rory Calloways
• Signed menus from our local chefs (Tobias Wrenfield, Calvin Morrow, Peter Hollis just to name a few) Trinkets from the Dunmore Market
• Pictures from a streetcar ride
• Indulge in a Korvan Beer or Rootbeer
• Try Granny Mabel’s Praline
• Sample Louisiana Gumbo

Local Attractions
• Hollowmere Heritage Museum
• Pellingham Institute-Zoo, Aquarium & Insectarium
• Whitcombe Cemetery #1
• Quillon Steamboat
• Dorvik’s Casino
• Brackwater Gallery of Fine Art
• St. Ambrel Catherdal
• The Marqueta
• Guthrie Street: best place to hear jazz
• Fernhollow Children’s Museum

Hotel Features
• Complimentary Wireless Internet Access
• Valet Parking
• 24 Hour Business Center
• Corvel’s Bar & Grill
• State of the Art Fitness Center
• Meeting Space—2 Rooms
• 24 Hour Room Service
• Grab n Go
• Pet Friendly

Nice to have
• Highlight Garden District location in New Orleans
Highlight close proximity to French Quarter, Central Business District and downtown
Streetcar Access to downtown
Pennick Street - has multitude of restaurants and shopping
Culture of New Orleans is throughout

```html
<!DOCTYPE html>
<html lang="en">
<head>
<meta charset="utf-8">
<title>Hotel Saffrine New Orleans Garden District – Fact Sheet</title>
<link rel="stylesheet" href="https://fonts.googleapis.com/css2?family=Arimo:ital,wght@0,400;0,700;1,400&display=swap">
<style>
  :root {
    --crimson: #d4104f;
    --ink: #111111;
    --text-grey: #6e7079;
    --label-grey: #7a7c85;
    --paper: #ffffff;
    --map-tone: #ebe6dc;
  }
  * { margin: 0; padding: 0; box-sizing: border-box; }
  html, body { width: 928px; height: 1200px; overflow: hidden; background: var(--paper); }
  body { font-family: "Arimo", Arial, Helvetica, sans-serif; color: var(--text-grey); }

  .sheet { position: relative; width: 928px; height: 1200px; background: var(--paper); }

  .top-band { position: absolute; left: 0; top: 0; width: 928px; height: 19px; background: var(--crimson); }

  .photo-strip { position: absolute; left: 0; top: 19px; width: 928px; height: 240px; display: flex; }
  .photo { height: 100%; }
  .photo--streetcar { width: 306px; background: linear-gradient(160deg, #6f7d5a 0%, #4b5a3e 45%, #7c6b5a 75%, #c27a8c 100%); }
  .photo--window { width: 306px; background: radial-gradient(circle at 50% 45%, #2f8c8a 0%, #3e6f6a 28%, #9c8a70 42%, #b9a68a 100%); }
  .photo--fence { width: 316px; background: linear-gradient(120deg, #4f7d2c 0%, #7fa84a 40%, #8e98a8 70%, #5f8a34 100%); }

  .headline {
    position: absolute; left: 69px; top: 301px; width: 820px; white-space: nowrap;
    font-weight: 700; font-size: 22px; line-height: 29.5px; color: var(--ink); letter-spacing: 1px;
  }

  .column { position: absolute; top: 380px; }
  .column--left { left: 69px; width: 390px; }
  .column--right { left: 473px; width: 400px; }

  .list-block { margin-bottom: 19px; }
  .list-block__title { font-weight: 700; font-size: 14.5px; line-height: 19.7px; color: var(--label-grey); }
  .feature-list { list-style: none; }
  .feature-list li {
    position: relative; padding-left: 15px;
    font-size: 13.9px; line-height: 19.65px; color: var(--text-grey);
  }
  .feature-list li::before {
    content: "\2724"; position: absolute; left: 0; top: 0;
    font-size: 12px; color: var(--text-grey);
  }

  .gds { position: absolute; left: 69px; top: 860px; font-size: 11.5px; color: var(--text-grey); white-space: nowrap; }
  .gds__title { position: absolute; left: 0; top: -1px; font-weight: 700; font-size: 13.5px; color: var(--label-grey); }
  .gds__item { position: absolute; top: 0; }
  .gds__item::before { content: "\2022"; margin-right: 4px; }
  .gds__item--1 { left: 97px; }
  .gds__item--2 { left: 216px; }
  .gds__item--3 { left: 364px; }
  .gds__item--4 { left: 505px; }
  .gds__item--5 { left: 624px; }

  .bottom-band { position: absolute; left: 0; top: 902px; width: 928px; height: 298px; background: var(--crimson); }

  .map { position: absolute; left: 44px; top: 942px; width: 540px; height: 219px; background: var(--map-tone); }

  .locator { position: absolute; left: 597px; top: 936px; color: var(--paper); width: 320px; }
  .locator__title { font-weight: 700; font-size: 34px; line-height: 40px; letter-spacing: -0.3px; }
  .locator__name { font-weight: 700; font-size: 13.5px; line-height: 17px; margin-top: 10px; }
  .locator__phone { font-size: 13.5px; line-height: 17px; }
  .locator__web { font-style: italic; font-size: 13px; line-height: 17px; }

  .contacts { margin-top: 20px; }
  .contacts__title { font-weight: 700; font-size: 12.5px; line-height: 16px; letter-spacing: 0.2px; }
  .contact { margin-top: 1px; margin-bottom: 2px; }
  .contact__name { font-weight: 700; font-size: 13px; line-height: 15.5px; }
  .contact__role { font-style: italic; font-size: 12px; line-height: 15.5px; }
</style>
</head>
<body>
<main class="sheet">
  <div class="top-band"></div>

  <section class="photo-strip">
    <div class="photo photo--streetcar" role="img" aria-label="Photo of a green streetcar passing pink flowering shrubs under oak trees"></div>
    <div class="photo photo--window" role="img" aria-label="Photo of a round stained glass window set in weathered wooden siding"></div>
    <div class="photo photo--fence" role="img" aria-label="Photo of an ornate iron fence against green foliage"></div>
  </section>

  <h1 class="headline">Located in the historic Garden District makes all destinations<br>in New Orleans just a short walk, ride or streetcar trip away.</h1>

  <div class="column column--left">
    <section class="list-block">
      <h2 class="list-block__title">Local Attractions:</h2>
      <ul class="feature-list">
        <li>Hollowmere Heritage Museum</li>
        <li>Pellingham Institute-Zoo, Aquarium &amp; Insectarium</li>
        <li>Quillon Steamboat</li>
        <li>Dorvik’s Casino</li>
        <li>Brackwater Gallery of Fine Art</li>
        <li>St. Ambrel Catherdal</li>
        <li>Tullis Square</li>
        <li>The Marqueta</li>
        <li>Fernhollow Children’s Museum</li>
      </ul>
    </section>
    <section class="list-block">
      <h2 class="list-block__title">Must Do:</h2>
      <ul class="feature-list">
        <li>Ride the Wexford Avenue Streetcar</li>
        <li>Shopping &amp; Dining on Pennick Street</li>
        <li>Eat beignets at Café Belvaro</li>
        <li>Garden District Tour—by foot or horse drawn carriage</li>
        <li>Visit Rory Calloways</li>
        <li>Tour the Hollowmere Heritage Museum</li>
        <li>Relax in Ashgrove Park</li>
        <li>Ride the Quillon Steamboat</li>
        <li>Visit St. Ambrel Cathedral</li>
        <li>Cemetery Tour</li>
      </ul>
    </section>
  </div>

  <div class="column column--right">
    <section class="list-block">
      <h2 class="list-block__title">Must See:</h2>
      <ul class="feature-list">
        <li>Garden District</li>
        <li>Pennick Street</li>
        <li>French Quarter</li>
        <li>Tamsin Street</li>
        <li>Art Galleries on Harrow Street</li>
        <li>Whitcombe Cemetery No. 1</li>
        <li>Guthrie Street: best place to hear jazz</li>
        <li>Dunmore Market</li>
      </ul>
    </section>
    <section class="list-block">
      <h2 class="list-block__title">Don’t Forget</h2>
      <ul class="feature-list">
        <li>Beignet mix from Café Belvaro</li>
        <li>Hurricane glass from Rory Calloways</li>
        <li>Signed menus from our local chefs (Tobias Wrenfield, Calvin Morrow, Peter Hollis just to name a few)</li>
        <li>Trinkets from the Dunmore Market</li>
        <li>Pictures from a streetcar ride</li>
        <li>Indulge in a Korvan Beer or Rootbeer</li>
        <li>Try Granny Mabel’s Praline</li>
        <li>Sample Louisiana Gumbo</li>
        <li>Mardi Gras Beads (available year round)</li>
      </ul>
    </section>
  </div>

  <section class="gds">
    <h2 class="gds__title">GDS CODES</h2>
    <span class="gds__item gds__item--1">Travora TA 493217</span>
    <span class="gds__item gds__item--2">Nimbra NM MSY427</span>
    <span class="gds__item gds__item--3">Routeway RW 7861</span>
    <span class="gds__item gds__item--4">Corsano CS 52648</span>
    <span class="gds__item gds__item--5">Veltrix VX MSYQV</span>
  </section>

  <div class="bottom-band"></div>

  <div class="map" role="img" aria-label="Street map of the Garden District showing the hotel location on Wexford Avenue"></div>

  <section class="locator">
    <h2 class="locator__title">We are here.</h2>
    <p class="locator__name">Hotel Saffrine New Orleans Garden District</p>
    <p class="locator__phone">504-718-2946</p>
    <p class="locator__web">www.hotelsaffrine.com/neworleansgdn</p>

    <div class="contacts">
      <h3 class="contacts__title">CONTACT INFORMATION</h3>
      <div class="contact">
        <p class="contact__name">Derek Manning</p>
        <p class="contact__role">General Manager</p>
      </div>
      <div class="contact">
        <p class="contact__name">Lydia Courten</p>
        <p class="contact__role">Director of Sales</p>
      </div>
      <div class="contact">
        <p class="contact__name">Karen Vosser</p>
        <p class="contact__role">Area Sales Manager</p>
      </div>
    </div>
  </section>
</main>
</body>
</html>
```